Ironvale Shift Services

We are a underground coal mining labour hire company, needing a website that links into our online payroll (www.wagetrakker.com.au) and also need to have job applications page that is a preform with drop down menu,s with answers or check boxes. We would also need a 3 tier administration access for access to different files.
We are looking for an ongoing relationship with future app integration

Reason: There are a few more designs to come and I'm out at the mine for another week

Industry/Entity Type

Coal Mining

```html
<!DOCTYPE html>
<html lang="en">
<head>
<meta charset="utf-8">
<title>Ironvale Shift Services</title>
<link href="https://fonts.googleapis.com/css2?family=Roboto+Condensed:wght@300;400;700&family=Open+Sans:wght@300;400;600;700&family=Arimo:wght@400;700&display=swap" rel="stylesheet">
<style>
:root{
  --orange:#f47c20;
  --orange-dark:#d9600c;
  --black:#000;
  --nav:#1c1c1c;
  --text:#444;
  --text-dark:#222;
  --white:#fff;
}
*{margin:0;padding:0;box-sizing:border-box}
html,body{width:960px;height:1200px;overflow:hidden}
body{position:relative;font-family:"Open Sans",sans-serif;color:var(--text);
  background:radial-gradient(ellipse at 50% 40%,#fff 0%,#f2f2f2 45%,#cfcfcf 100%)}
.abs{position:absolute}
/* header */
.masthead{left:0;top:0;width:960px;height:240px;background:var(--black)}
.brand{left:92px;top:12px;width:172px;height:188px;background:#050505;display:flex;flex-direction:column;align-items:center;justify-content:center;gap:12px}
.brand-dot{width:54px;height:54px;border-radius:50%;background:var(--orange)}
.brand-name{font-family:"Arimo",sans-serif;font-size:11px;color:var(--orange);text-align:center}
.contact{left:632px;top:15px;width:240px}
.contact-row{display:flex;gap:10px;margin-bottom:18px}
.contact-icon{width:20px;height:20px;background:var(--orange);flex:none;margin-top:4px;display:flex;align-items:center;justify-content:center}
.contact-text{font-family:"Arimo",sans-serif;font-size:10.5px;line-height:18px;color:#bbb}
.search{left:592px;top:162px;width:246px;height:35px;background:linear-gradient(#555,#2e2e2e);clip-path:polygon(24px 0,100% 0,100% 100%,0 100%)}
.search-field{left:632px;top:168px;width:146px;height:22px;border-radius:3px;background:#777;box-shadow:inset 0 1px 3px #222}
.search-btn{left:777px;top:168px;width:54px;height:22px;background:var(--orange);color:#fff;font-family:"Arimo",sans-serif;font-size:10px;line-height:22px;text-align:center;border-radius:0 3px 3px 0}
/* nav */
.nav{left:114px;top:202px;width:725px;height:38px;background:var(--nav);display:flex;align-items:center;justify-content:space-around;padding:0 6px}
.nav a{font-family:"Arimo",sans-serif;font-size:9.5px;color:#fff;text-decoration:none;padding:7px 7px;border-radius:3px}
.nav a.active{background:var(--orange);box-shadow:0 0 0 1px #ffb070 inset}
.submenu{left:308px;top:242px;width:142px;height:102px;background:#000;padding:5px 4px;z-index:3}
.submenu div{height:30px;font-family:"Times New Roman",serif;font-size:11px;color:#fff;line-height:28px;padding-left:26px;border-bottom:1px solid #444;position:relative}
.submenu div::before{content:"»";position:absolute;left:10px}
.submenu div.on{background:var(--orange)}
/* hero */
.hero{left:114px;top:242px;width:725px;height:308px;background:linear-gradient(160deg,#6a3e10 0%,#a4661c 40%,#5a3410 75%,#2a1808 100%)}
.caption{left:114px;top:500px;width:725px;height:50px;background:rgba(30,30,30,.88);display:flex;align-items:center}
.caption p{width:665px;text-align:center;font-family:"Open Sans",sans-serif;font-weight:300;font-size:17.5px;color:#bbb}
.caption b{color:#ccc;font-weight:600}
.arrow{width:30px;height:50px;border-left:1px solid #333;display:flex;align-items:center;justify-content:center}
/* columns */
.col{top:550px;height:232px;padding:16px 19px}
.col h2{font-family:"Roboto Condensed",sans-serif;font-weight:400;font-size:17px;color:var(--text-dark)}
.col h2 span{color:var(--orange)}
.hiring{left:114px;width:236px;background:linear-gradient(#e4e4e4,#dcdcdc)}
.solutions{left:350px;width:251px;background:linear-gradient(#dedede,#d6d6d6)}
.login{left:601px;width:238px;background:linear-gradient(#e6e6e6,#dedede)}
.hiring p{margin-top:18px;font-size:10.3px;line-height:20px;color:#555}
.solutions ul{list-style:none;margin-top:14px}
.solutions li{font-size:9px;line-height:14.5px;color:#444;padding-left:12px;position:relative;margin-bottom:14px}
.solutions li::before{content:"";position:absolute;left:0;top:4px;width:6px;height:6px;border-radius:50%;background:var(--orange);box-shadow:0 0 0 1px #f8c08a}
.login .label{font-size:10px;color:#333;margin:14px 0 8px 12px}
.field{margin-left:12px;width:167px;height:28px;border-radius:6px;background:#fff;border:1px solid #ccc;font-size:9px;color:#444;padding:8px 14px;margin-bottom:7px}
.field.tall{height:52px}
.submit{margin:3px 0 0 90px;width:89px;height:26px;border-radius:5px;background:linear-gradient(#ff9a3c,var(--orange-dark));color:#fff;font-size:13px;text-align:center;line-height:26px;font-weight:600}
/* products */
.products{left:114px;top:782px;width:725px;height:330px;background:#fff}
.prod-title{left:120px;top:798px;font-family:"Roboto Condensed",sans-serif;font-weight:400;font-size:24px;color:#222}
.prod-title span{font-family:"Open Sans",sans-serif;font-weight:400;font-size:14px;margin-left:6px}
.prod-photo{left:122px;top:842px;width:516px;height:166px;background:linear-gradient(180deg,#bdbdbd,#6a6a6a 60%,#9a9a9a)}
.prod-text{left:124px;top:1018px;width:470px;font-family:"Arimo",sans-serif;font-size:10.4px;line-height:17.6px;color:#333}
.prod-text a{color:var(--orange);font-weight:700}
.dl-box{left:665px;top:840px;width:168px;height:168px;background:linear-gradient(#e8e8e8,#d2d2d2);border:1px solid #ccc;padding:6px 8px}
.dl-box h3{font-family:"Roboto Condensed",sans-serif;font-weight:700;font-size:23px;color:var(--orange);line-height:26px}
.dl-box h4{font-family:"Roboto Condensed",sans-serif;font-weight:700;font-size:15px;color:#222;line-height:20px;margin-top:2px}
.dl-count{font-size:8px;color:#555;margin:6px 0 4px 4px;display:flex;align-items:center;gap:6px}
.tick{width:10px;height:10px;border:1px solid #999;background:#fff;display:flex;align-items:center;justify-content:center}
.dl-btn{width:142px;height:40px;border-radius:5px;background:linear-gradient(#a4e05a,#4aa81c);color:#fff;font-family:"Open Sans",sans-serif;font-size:16px;line-height:40px;padding-left:46px;position:relative}
.dl-btn::before{content:"";position:absolute;left:10px;top:6px;width:26px;height:28px;background:#f0f0f0;border-radius:3px}
.social{top:1030px;width:24px;height:24px;border-radius:50%;background:#c9c9c9;box-shadow:0 1px 2px #888}
/* footer */
.footer{left:114px;top:1112px;width:725px;height:85px;background:linear-gradient(#d6d6d6,#c4c4c4);border-top:3px solid #1a1a1a;box-shadow:0 -2px 0 var(--orange) inset}
.footer-rule{left:114px;top:1115px;width:725px;height:2px;background:var(--orange)}
.footer-links{left:141px;top:1143px;font-family:"Arimo",sans-serif;font-size:9.5px;color:#333}
.footer-copy{left:141px;top:1162px;font-family:"Arimo",sans-serif;font-size:9.5px;color:#333}
.footer-brand{left:618px;top:1128px;display:flex;align-items:center;gap:10px}
.footer-brand i{width:60px;height:60px;border-radius:50%;border:3px solid #fff}
.footer-brand span{font-family:"Arimo",sans-serif;font-size:15px;color:#fff;width:110px;line-height:18px}
</style>
</head>
<body>
<header class="masthead abs"></header>
<div class="brand abs"><i class="brand-dot"></i><span class="brand-name">Ironvale Shift Services</span></div>

<div class="contact abs">
  <div class="contact-row"><span class="contact-icon"><svg width="10" height="10" viewBox="0 0 10 10"><path d="M2 1l2 2-1 1.5c.6 1.2 1.3 1.9 2.5 2.5L7 6l2 2-1.5 1.5C4 9 1 6 .5 2.5z" fill="#fff"/></svg></span><p class="contact-text">Redgum Workhouse 42 Ridge Street,<br>Newcastle, NSW 2300</p></div>
  <div class="contact-row"><span class="contact-icon"><svg width="10" height="10" viewBox="0 0 10 10"><path d="M5 1L1 5h1.3v4h2V6.5h1.4V9h2V5H9z" fill="#fff"/></svg></span><p class="contact-text">Phone: +61 2 4900 1100<br>Fax: +61 2 4900 1101</p></div>
  <div class="contact-row"><span class="contact-icon"><svg width="10" height="8" viewBox="0 0 10 8"><rect x=".5" y=".5" width="9" height="7" fill="#fff"/><path d="M.5 .5L5 4.5 9.5 .5" stroke="#f47c20" fill="none"/></svg></span><p class="contact-text">Email: info@ironvaleshift.au<br>Web: www.ironvaleshift.au</p></div>
</div>

<div class="search abs"></div>
<svg class="abs" style="left:610px;top:170px" width="16" height="18" viewBox="0 0 16 18"><circle cx="10" cy="6" r="4.5" stroke="#777" stroke-width="2" fill="none"/><path d="M7 9L2 16" stroke="#777" stroke-width="2.5"/></svg>
<div class="search-field abs"></div>
<div class="search-btn abs">SEARCH</div>

<nav class="nav abs">
  <a href="#">HOME</a><a href="#">ABOUT US</a><a href="#" class="active">CAREERS ▾</a><a href="#">SERVICES &nbsp;▾</a><a href="#">INNOVATION</a><a href="#">NEWS</a><a href="#">PRODUCTS</a><a href="#">CONTACT</a>
</nav>

<div class="hero abs" role="img" aria-label="Photo of an open-cut quarry with stone blocks and an orange excavator"></div>
<div class="submenu abs"><div class="on">Lorem Ipsum,</div><div>Lorem Ipsum</div><div>Lorem Ipsum</div></div>
<div class="caption abs">
  <p>The standard <b>chunk of Lorem Ipsum</b> used since the 1500s is reproduced</p>
  <span class="arrow"><svg width="10" height="20" viewBox="0 0 10 20"><path d="M9 1L1 10l8 9" stroke="#888" fill="none"/></svg></span>
  <span class="arrow"><svg width="10" height="20" viewBox="0 0 10 20"><path d="M1 1l8 9-8 9" stroke="#888" fill="none"/></svg></span>
</div>

<section class="col hiring abs">
  <h2>Labour &nbsp;<span>Hiring</span></h2>
  <p>The standard chunk of Lorem Ipsum used since the 1500s is reproduced below for those interested. Sections and from "de Finibus Bonorum et Malorum" by Cicero are also chunk of Lorem Ipsum used since the 1500s is reproduced below in their exact original form</p>
</section>
<section class="col solutions abs">
  <h2>Labour <span>Solutions</span></h2>
  <ul>
    <li>At est option labitur detracto, pro cu amet veritus epicurei. Sensibus honestatis perseq</li>
    <li>At est option labitur detracto, pro cu amet veritus epicurei. Sensibus honestatis perseq</li>
    <li>At est option labitur detracto, pro cu amet veritus epicurei. Sensibus honestatis perseq</li>
    <li>At est option labitur detracto, pro cu amet veritus epicurei. Sensibus honestatis perseq</li>
  </ul>
</section>
<section class="col login abs">
  <h2>Employees <span>Login</span></h2>
  <p class="label">Login Now</p>
  <div class="field">----Name----</div>
  <div class="field">----Email----</div>
  <div class="field tall">---- Your Message ------</div>
  <div class="submit">Submit</div>
</section>

<section class="products abs"></section>
<h2 class="prod-title abs">Products Informations<span>Take all products information from here.</span></h2>
<div class="prod-photo abs" role="img" aria-label="Black and white photo of an excavator on a construction site"></div>
<p class="prod-text abs">To allow Fieldlink Market to update the stats in your marketing campaigns, we’ll need you to create an integrator username and password within Crewlattice Console. It only takes 1 minute and the steps are below, alternativley <a href="#">click here</a> to view a quick video:</p>
<div class="dl-box abs">
  <h3>DOWNLOAD!</h3>
  <h4>INFORMATION OF THE PRODUCTS AND THE APPLICATION</h4>
  <div class="dl-count"><span class="tick"><svg width="8" height="7" viewBox="0 0 8 7"><path d="M1 3.5l2 2L7 1" stroke="#f47c20" stroke-width="1.5" fill="none"/></svg></span>1.3456 downloads</div>
  <div class="dl-btn">Download</div>
</div>
<span class="social abs" style="left:670px"></span>
<span class="social abs" style="left:705px"></span>
<span class="social abs" style="left:740px"></span>
<span class="social abs" style="left:776px"></span>

<footer class="footer abs"></footer>
<div class="footer-rule abs"></div>
<p class="footer-links abs">Home | About Us | Returns | Payment | Shipping | Feedback | Contact Us</p>
<p class="footer-copy abs">Copyright © 2014 Harbour Line Sales. All rights reserved. &nbsp;| &nbsp;Storefront Template Design</p>
<div class="footer-brand abs"><i></i><span>Ironvale Shift Services</span></div>
</body>
</html>
```